BHSC Business cards

We are an established dental practice that is looking for new business cards to match our new logo. We are looking for something unique and sophisticated.
BRIEF: Colours are black, silver and white. Include the company name, logo (including “Pelwick Heath Dental Care”) and phone number “03 9415 2876”.
Front - Include the company name, logo (including “Pelwick Heath Dental Care”) and phone number “03 9415 2876”.
Back - Include the company name,  “Pelwick Heath Dental Care”, phone number “03 9415 2876”. address "64A Tindle Street, Pelwick Heath, Vic 3187", "Email reception@pelwickheathdentalcare.com.au", the Dentist Name " Dr ................................"  Your next appointment "Day, date and time(am/pm)".  3 lines for 3 appointments please, and at the bottom "IF UNABLE TO KEEP THIS APPOINTMENT 48 HOURS NOTICE IS REQUIRED."
Try and be creative and different with the design, i've added an image for inspiration

Target Market(s)
ALL in need of dental
Industry/Entity Type
Dental Clinic
Look and feel
Each slider illustrates characteristics of the customer's brand and the style your logo design should communicate.

```html
<!DOCTYPE html>
<html lang="en">
<head>
<meta charset="utf-8">
<title>Pelwick Heath Dental Care – Business Cards</title>
<link rel="stylesheet" href="https://fonts.googleapis.com/css2?family=Montserrat:wght@600;700&family=Jost:wght@300;400;500;600&display=swap">
<style>
  :root {
    --ink: #1a1a1a;
    --paper: #ffffff;
    --silver: #f3f4f6;
    --backdrop: #c9c9c9;
    --rule: #8a8a8a;
  }
  * { margin: 0; padding: 0; box-sizing: border-box; }
  html, body { width: 1125px; height: 1200px; overflow: hidden; }
  body { background: var(--backdrop); position: relative; font-family: "Jost", sans-serif; color: var(--ink); }

  .card { position: absolute; left: 178px; width: 768px; height: 437px; background: var(--paper); border-radius: 16px; overflow: hidden; }
  .card--front { top: 140px; }
  .card--back { top: 627px; }

  /* Brand lockup */
  .brand { position: absolute; display: flex; align-items: center; }
  .brand__mark { border: 3px solid var(--ink); border-radius: 50%; flex: none; }
  .brand__text { font-family: "Montserrat", sans-serif; font-weight: 700; color: var(--ink); line-height: 1; }
  .brand__name { display: block; }
  .brand__sub { display: block; letter-spacing: 0.28em; }
  .brand__phone { font-family: "Montserrat", sans-serif; font-weight: 700; letter-spacing: 0.06em; }

  .card--front .brand { left: 139px; top: 120px; }
  .card--front .brand__mark { width: 104px; height: 104px; border-width: 4px; margin-right: 22px; }
  .card--front .brand__name { font-size: 49px; letter-spacing: 0.01em; }
  .card--front .brand__sub { font-size: 22px; margin-top: 8px; }
  .card--front .brand__phone { font-size: 22px; letter-spacing: 0.08em; }

  .front-phone { position: absolute; left: 133px; top: 304px; display: flex; align-items: center; }
  .front-phone__icon { width: 72px; height: 72px; border-radius: 50%; background: var(--ink); display: flex; align-items: center; justify-content: center; margin-right: 22px; }
  .front-phone__number { font-family: "Montserrat", sans-serif; font-weight: 700; font-size: 62px; letter-spacing: 0.01em; }

  /* Back */
  .back__details { position: absolute; left: 0; top: 0; width: 455px; height: 100%; background: var(--silver); }
  .dentist { position: absolute; left: 28px; top: 52px; }
  .dentist__name { font-weight: 600; font-size: 27px; line-height: 1.1; }
  .dentist__role { font-weight: 300; font-size: 21px; margin-top: 2px; }
  .address { position: absolute; left: 28px; top: 202px; font-size: 18.5px; font-weight: 300; line-height: 1.25; }
  .contacts { position: absolute; left: 28px; top: 262px; list-style: none; font-size: 18.5px; font-weight: 300; }
  .contacts li { display: flex; align-items: center; height: 27px; }
  .contacts svg { width: 14px; height: 14px; margin-right: 6px; flex: none; }

  .card--back .brand { left: 468px; top: 52px; }
  .card--back .brand__mark { width: 48px; height: 48px; border-width: 2px; margin-right: 10px; }
  .card--back .brand__name { font-size: 22.5px; }
  .card--back .brand__sub { font-size: 10.5px; margin-top: 3px; letter-spacing: 0.24em; }
  .card--back .brand__phone { font-size: 10.5px; }

  .appointment { position: absolute; left: 468px; top: 140px; width: 272px; }
  .appointment__title { font-size: 15px; font-weight: 400; letter-spacing: 0.01em; }
  .appointment__line { border-bottom: 1px dashed var(--rule); height: 1px; }
  .appointment__line--1 { margin-top: 27px; }
  .appointment__line--2 { margin-top: 36px; }
  .slots { list-style: none; margin-top: 38px; font-size: 13px; font-weight: 300; }
  .slot { display: flex; align-items: baseline; height: 31px; }
  .slot__fill { border-bottom: 1px dashed var(--rule); height: 1px; align-self: flex-end; margin: 0 4px 9px; }
  .slot__fill--date { width: 82px; }
  .slot__fill--time { width: 82px; }

  .notice { position: absolute; left: 0; top: 368px; width: 100%; height: 41px; background: var(--ink); color: var(--paper); font-size: 17.5px; font-weight: 300; text-align: center; line-height: 41px; letter-spacing: 0.01em; }
</style>
</head>
<body>

<section class="card card--front">
  <div class="brand">
    <div class="brand__mark"></div>
    <div class="brand__text">
      <span class="brand__name">PELWICK HEATH</span>
      <span class="brand__sub">DENTAL CARE<span class="brand__phone"> — 03 9415 2876</span></span>
    </div>
  </div>
  <div class="front-phone">
    <div class="front-phone__icon">
      <svg width="40" height="32" viewBox="0 0 40 32" aria-hidden="true">
        <path d="M3 9 C3 2 37 2 37 9 L37 12 L29 12 L29 8 L11 8 L11 12 L3 12 Z" fill="#fff"/>
        <path d="M11 12 L29 12 L36 22 L36 29 L4 29 L4 22 Z" fill="#fff"/>
        <g fill="#1a1a1a"><circle cx="16" cy="17" r="1.3"/><circle cx="20" cy="17" r="1.3"/><circle cx="24" cy="17" r="1.3"/><circle cx="16" cy="21" r="1.3"/><circle cx="20" cy="21" r="1.3"/><circle cx="24" cy="21" r="1.3"/><circle cx="16" cy="25" r="1.3"/><circle cx="20" cy="25" r="1.3"/><circle cx="24" cy="25" r="1.3"/></g>
      </svg>
    </div>
    <span class="front-phone__number">03 9415 2876</span>
  </div>
</section>

<section class="card card--back">
  <div class="back__details">
    <div class="dentist">
      <p class="dentist__name">Dr Marcus Trelane</p>
      <p class="dentist__role">Dentist</p>
    </div>
    <p class="address">64A Tindle Street,<br>Pelwick Heath, Vic 3187</p>
    <ul class="contacts">
      <li><svg viewBox="0 0 16 16" aria-hidden="true"><path d="M3 1 L6 1 L7 5 L5 6.5 C6 9 7 10 9.5 11 L11 9 L15 10 L15 13 C15 14 14 15 13 15 C6 15 1 10 1 3 C1 2 2 1 3 1 Z" fill="#1a1a1a"/></svg>03 9415 2876</li>
      <li><svg viewBox="0 0 16 16" aria-hidden="true"><rect x="1" y="3" width="14" height="10" fill="#1a1a1a"/><path d="M1 3 L8 9 L15 3" stroke="#f3f4f6" stroke-width="1.2" fill="none"/></svg>reception@pelwickheathdentalcare.com.au</li>
      <li><svg viewBox="0 0 16 16" aria-hidden="true"><circle cx="8" cy="8" r="7" fill="#1a1a1a"/><path d="M4 5 C6 5 7 7 6 9 M10 3 C9 6 12 7 13 9" stroke="#f3f4f6" stroke-width="1.2" fill="none"/></svg>pelwickheathdentalcare.com.au</li>
    </ul>
  </div>

  <div class="brand">
    <div class="brand__mark"></div>
    <div class="brand__text">
      <span class="brand__name">PELWICK HEATH</span>
      <span class="brand__sub">DENTAL CARE<span class="brand__phone"> — 03 9415 2876</span></span>
    </div>
  </div>

  <div class="appointment">
    <p class="appointment__title">NEXT APPOINTMENT</p>
    <div class="appointment__line appointment__line--1"></div>
    <div class="appointment__line appointment__line--2"></div>
    <ul class="slots">
      <li class="slot">Date<span class="slot__fill slot__fill--date"></span>At<span class="slot__fill slot__fill--time"></span>am/pm</li>
      <li class="slot">Date<span class="slot__fill slot__fill--date"></span>At<span class="slot__fill slot__fill--time"></span>am/pm</li>
      <li class="slot">Date<span class="slot__fill slot__fill--date"></span>At<span class="slot__fill slot__fill--time"></span>am/pm</li>
    </ul>
  </div>

  <p class="notice">IF UNABLE TO KEEP THIS APPOINTMENT 48 HOURS NOTICE IS REQUIRED</p>
</section>

</body>
</html>
```